New nutrition counseling business needs a flyer and logo design for marketing purposes

Need a new flyer for distribution to advertise and inform the public about new Dietetic Counseling service. The new business name is Harbor of Vigor with “Harbor” being the main name. It will provide nutrition consultation services to individuals who seek to change their dietary habits to achieve a variety of different health objectives. These objectives can include, but are not limited to weight management, enhanced athletic performance, improved health biomarkers, and reducing the risks or symptoms of chronic nutrition related diseases. The services provided include direct one on one counseling that entails health and nutrition assessments, evaluation of goals, and the determination of strategies to meet these goals. We would like to see designs that use an ocean color scheme with purple aspects as well. Color and logo ideas attached in uploads. Please include logo on the flyer as well.

Target Market(s)

General Population

Colors
0094D4
00A9DD
6FCCEA
C7EBF8
E9F6FB
00AB8E
00BBA5
67D7C9
C6EFE9
E9F9F6
6B429C
8869AF
B7A5CE
E3DAEB
F3F0F8

Requirements
Nice to have
• Pictures of nourishing foods, fruits, vegetables etc.
Should not have
• Do not include people in flyer or logo design

```html
<!DOCTYPE html>
<html lang="en">
<head>
<meta charset="utf-8">
<title>Harbor of Vigor – Nutrition Counseling Flyer</title>
<link rel="stylesheet" href="https://fonts.googleapis.com/css2?family=Roboto+Condensed:wght@300;400;700&family=Archivo:wght@800&family=Arimo:wght@400;700&display=swap">
<style>
  :root {
    --ink: #4a5a4c;
    --white: #ffffff;
    --sky-light: #e6f5f8;
    --sky-right: #5fbccc;
    --teal: #00ab8e;
    --name-ink: #243a33;
    --contact-blue: #2fb8ec;
    --rule: #7fc3cf;
    --plate: #f7f9f9;
    --greens: #8fc25a;
  }
  * { margin: 0; padding: 0; box-sizing: border-box; }
  html, body { width: 927px; height: 1200px; overflow: hidden; }
  body { font-family: "Roboto Condensed", "Arial Narrow", sans-serif; color: var(--ink); }

  .flyer {
    position: relative;
    width: 927px; height: 1200px;
    overflow: hidden;
    background:
      radial-gradient(ellipse 520px 420px at 40px 470px, var(--sky-light) 0%, rgba(230,245,248,0) 100%),
      linear-gradient(100deg, #bfe6ee 0%, #9fd8e4 55%, var(--sky-right) 100%);
  }
  .flyer > * { z-index: 2; }

  .salad-photo {
    position: absolute; left: -6px; top: 470px; z-index: 1;
    width: 934px; height: 934px; border-radius: 50%;
    background:
      radial-gradient(circle at 50% 62%, #6ea84a 0%, var(--greens) 34%, #c6dd9a 46%, rgba(247,249,249,0.96) 56%, rgba(247,249,249,0.85) 100%);
  }

  .brand-title {
    position: absolute; top: 34px; left: 0; width: 100%;
    text-align: center;
    font-weight: 700; font-size: 66px; letter-spacing: 0.5px; line-height: 1;
    color: var(--ink);
  }
  .brand-title .joiner { font-size: 32px; }

  .headline {
    position: absolute; top: 118px; left: 0; width: 100%;
    text-align: center; color: var(--white);
    font-weight: 400; font-size: 70px; line-height: 58px;
    letter-spacing: 0.5px;
  }
  .tagline {
    position: absolute; top: 258px; left: 0; width: 100%;
    text-align: center;
    font-family: "Archivo", "Arial Black", sans-serif; font-weight: 800;
    font-size: 35px; letter-spacing: 0.6px; color: var(--ink);
  }

  .services-heading {
    position: absolute; top: 316px; left: 98px;
    font-weight: 700; font-size: 23px;
  }
  .services-rule {
    position: absolute; top: 351px; left: 98px; width: 728px; height: 2px;
    background: linear-gradient(90deg, var(--rule), rgba(127,195,207,0.2));
  }
  .services-list {
    position: absolute; top: 366px; left: 97px;
    list-style: none; font-size: 17px; font-weight: 400;
  }
  .services-list li { height: 25.8px; line-height: 25.8px; white-space: nowrap; }
  .services-list li::before { content: "•"; margin-right: 8px; }
  .consult-note {
    position: absolute; top: 559px; left: 96px;
    font-weight: 700; font-size: 18.5px; letter-spacing: 0.2px;
  }

  .owner-badge {
    position: absolute; left: 605px; top: 416px; z-index: 3;
    width: 275px; height: 275px; border-radius: 50%;
    background: var(--teal); text-align: center;
  }
  .owner-label {
    margin-top: 48px;
    display: flex; justify-content: center; align-items: center; gap: 8px;
    font-family: "Arimo", sans-serif; font-weight: 700; font-size: 15px; color: var(--white);
  }
  .owner-label svg { display: block; }
  .owner-name {
    margin-top: 8px;
    font-weight: 700; font-size: 26px; color: var(--name-ink); line-height: 1;
    white-space: nowrap;
  }
  .owner-credentials {
    margin-top: 10px;
    font-size: 16px; line-height: 20px; color: var(--white);
  }
  .owner-credentials small { font-size: 12px; }
  .owner-license {
    margin-top: 38px; font-size: 12.5px; color: var(--white);
  }

  .contact-band {
    position: absolute; left: 0; top: 1052px; z-index: 3;
    width: 927px; height: 148px;
    background: var(--ink); color: var(--white); text-align: center;
    font-family: "Arimo", Arial, sans-serif;
  }
  .contact-invite {
    margin-top: 22px; font-size: 21.5px; line-height: 26px; letter-spacing: 0.2px;
  }
  .contact-invite strong { font-weight: 700; }
  .contact-details {
    margin-top: 10px;
    font-weight: 700; font-size: 31px; color: var(--contact-blue); letter-spacing: 0.3px;
  }
  .contact-details .divider { margin: 0 34px; }
</style>
</head>
<body>
<main class="flyer">
  <div class="salad-photo" role="img" aria-label="Photo of a fresh green salad with tomatoes, radish, carrots and black olives on a white plate"></div>

  <h1 class="brand-title">HARBOR <span class="joiner">OF</span> VIGOR</h1>

  <p class="headline">FOSTER POSITIVE<br>NUTRITION PRACTICES</p>
  <p class="tagline">FOR A HEALTHIER LIFESTYLE</p>

  <h2 class="services-heading">Services</h2>
  <div class="services-rule"></div>
  <ul class="services-list">
    <li>Medical Nutrition Therapy for chronic conditions such as diabetes, hypertension, high cholesterol, and more</li>
    <li>Weight Management</li>
    <li>Healthy Eating and Meal Planning</li>
    <li>Nutrition for Athletic Performance</li>
    <li>Pre and Post Natal Nutrition</li>
    <li>Personalized meal plans uniquely catered to each individual</li>
    <li>Highly collaborative approach to help you meet your goals</li>
  </ul>
  <p class="consult-note">BOTH IN PERSON AND VIRTUAL CONSULTATIONS ARE OFFERED</p>

  <section class="owner-badge">
    <div class="owner-label">
      <svg width="38" height="10" viewBox="0 0 38 10"><path d="M1 6 Q10 0 19 5 T37 3" fill="none" stroke="#c6efe9" stroke-width="1.4"/></svg>
      OWNER
      <svg width="38" height="10" viewBox="0 0 38 10"><path d="M1 3 Q10 0 19 5 T37 6" fill="none" stroke="#c6efe9" stroke-width="1.4"/></svg>
    </div>
    <div class="owner-name">MARISOL DUNLEAVY</div>
    <p class="owner-credentials">Master of Science in Dietetics and<br>Nutrition, Registered Dietitian <small>(RD)</small>,<br>Licensed Dietitian Nutritionist <small>(LDN)</small></p>
    <p class="owner-license">License Number:&nbsp; ND 40219.</p>
  </section>

  <footer class="contact-band">
    <p class="contact-invite"><strong>LET’S CHAT!</strong> FREE 15-MINUTE INTRODUCTORY CONSULTATION<br>TO DISCUSS PROGRAM DETAILS AND RATES</p>
    <p class="contact-details">555-014-2287<span class="divider">|</span>MARISOL@HARBORRD.NET</p>
  </footer>
</main>
</body>
</html>
```